Handout Flyer For Medical Practice (This is Exciting!)

We need a single page handout that showcases the doctors in our medical practice and their specific specialities.

On the front I would like the pictures of the Doctors, names and their specialties. One the back, Map and Contact information for the practice

Attached in the files is what we are currently using and we do want anything that looks such as that.

Industry/Entity Type

Medical

Font styles to use
Serif

Colors
3176b5
0456a4

Requirements
Must have
• Up to date look. Would like a modern touch.

```html
<!DOCTYPE html>
<html lang="en">
<head>
<meta charset="utf-8">
<title>Northgate Bone &amp; Spine Care Center – Handout</title>
<link href="https://fonts.googleapis.com/css2?family=Tinos:wght@400;700&family=Arimo:wght@400;700&display=swap" rel="stylesheet">
<style>
  :root {
    --brand-blue: #0456a4;
    --brand-mid: #3176b5;
    --brand-deep: #0b2f6e;
    --navy: #061a3a;
    --navy-2: #0a2350;
    --backdrop: #f1f1f3;
    --white: #ffffff;
    --silver: #c9ccd2;
    --photo-bg: #6d7f92;
    --map-tone: #e8e4dc;
  }
  * { margin: 0; padding: 0; box-sizing: border-box; }
  html, body { width: 1200px; height: 1000px; overflow: hidden; }
  body { background: var(--backdrop); position: relative; font-family: "Arimo", Arial, sans-serif; }

  .page { position: absolute; overflow: hidden; background: var(--white); }
  .page--front { left: 109px; top: 140px; width: 483px; height: 625px; }
  .page--back { left: 640px; top: 222px; width: 477px; height: 620px; }

  .brand { position: absolute; left: 0; right: 0; text-align: center; color: var(--brand-blue); }
  .brand__name { font-family: "Tinos", "Times New Roman", serif; font-weight: 700; line-height: 1.05; }
  .brand__name-row { display: flex; align-items: center; justify-content: center; gap: 8px; }
  .brand__dot { width: 14px; height: 14px; border-radius: 50%; background: var(--brand-mid); flex: none; }
  .brand__sub { font-weight: 700; }
  .brand__line { font-weight: 400; }
  .brand__phone { font-weight: 700; }

  .front-brand { top: 22px; }
  .front-brand .brand__name { font-size: 24px; }
  .front-brand .brand__sub { font-size: 12.5px; margin-top: 4px; }
  .front-brand .brand__line { font-size: 12.5px; margin-top: 2px; }
  .front-brand .brand__phone { font-size: 12.5px; margin-top: 2px; }

  .front-backdrop { position: absolute; left: 0; top: 0; width: 483px; height: 625px; }

  .team { position: absolute; left: 33px; top: 167px; width: 415px; display: grid;
          grid-template-columns: repeat(4, 96px); column-gap: 10px; row-gap: 18px; }
  .doctor { text-align: center; color: var(--white); }
  .doctor__photo { width: 96px; height: 138px; background: linear-gradient(180deg, #8a98a8, #4a5768); }
  .doctor__photo--dark { background: #231f20; }
  .doctor__name { font-size: 7px; font-weight: 700; margin-top: 5px; white-space: nowrap; }
  .doctor__role { font-size: 5.6px; font-style: italic; line-height: 1.25; margin-top: 1px; }

  .about { position: absolute; left: 30px; right: 30px; top: 543px; color: var(--white);
           font-size: 8.6px; line-height: 1.3; text-align: center; }

  .back-header { position: absolute; left: 0; top: 0; width: 477px; height: 130px; }
  .back-title { position: absolute; left: 0; right: 0; top: 30px; text-align: center;
                font-family: "Tinos", "Times New Roman", serif; font-size: 42px; color: var(--white); }
  .map { position: absolute; left: 0; top: 100px; width: 477px; height: 266px;
         background: linear-gradient(160deg, #ece8e1, var(--map-tone) 60%, #ddd8ce); }
  .map-cover { position: absolute; left: 0; top: 0; width: 477px; height: 130px; pointer-events: none; }
  .silver-strip { position: absolute; left: 0; top: 366px; width: 477px; height: 10px;
                  background: linear-gradient(90deg, #e8eaee, var(--silver) 50%, #f4f5f7); }

  .back-brand { top: 392px; }
  .back-brand .brand__name { font-size: 28px; }
  .back-brand .brand__sub { font-size: 14px; margin-top: 6px; }
  .back-brand .brand__line { font-size: 14px; margin-top: 3px; }
  .back-brand .brand__phone { font-size: 14px; margin-top: 3px; }

  .callout { position: absolute; left: 0; top: 526px; width: 477px; height: 94px;
             background: var(--brand-blue); color: var(--white); text-align: center; }
  .callout__main { font-family: "Tinos", "Times New Roman", serif; font-weight: 700; font-size: 26px; margin-top: 17px; }
  .callout__main span { font-size: 29px; }
  .callout__hours { font-size: 13.5px; font-weight: 700; margin-top: 2px; }
</style>
</head>
<body>

<section class="page page--front" aria-label="Front: our doctors">
  <svg class="front-backdrop" viewBox="0 0 483 625" aria-hidden="true">
    <defs>
      <linearGradient id="frontBlue" x1="0" y1="0" x2="1" y2="1">
        <stop offset="0" stop-color="#0a2a66"/>
        <stop offset="0.4" stop-color="#1f5fc0"/>
        <stop offset="0.7" stop-color="#0c3a8a"/>
        <stop offset="1" stop-color="#061a3a"/>
      </linearGradient>
      <linearGradient id="silverEdge" x1="0" y1="0" x2="1" y2="0">
        <stop offset="0" stop-color="#ffffff"/>
        <stop offset="0.5" stop-color="#b8bcc4"/>
        <stop offset="1" stop-color="#ffffff"/>
      </linearGradient>
    </defs>
    <rect x="0" y="120" width="483" height="410" fill="url(#frontBlue)"/>
    <path d="M0 150 C120 120 260 110 483 140 L483 120 L0 120 Z" fill="url(#silverEdge)"/>
    <path d="M0 145 C130 118 270 112 483 132 L483 0 L0 0 Z" fill="#ffffff"/>
    <rect x="0" y="527" width="483" height="4" fill="url(#silverEdge)"/>
    <rect x="0" y="531" width="483" height="94" fill="#071c40"/>
  </svg>

  <header class="brand front-brand">
    <div class="brand__name-row"><span class="brand__dot"></span><div class="brand__name">Northgate Bone &amp; Spine<br>Care Center</div></div>
    <p class="brand__sub">Northgate Bone &amp; Spine Care Center</p>
    <p class="brand__line">2450 W. Meadow Road, Ste. 210, Riverton, MO 63999</p>
    <p class="brand__phone">Phone: 555-204-7731 | www.ngspine.com</p>
  </header>

  <div class="team">
    <article class="doctor"><div class="doctor__photo" role="img" aria-label="Portrait photo of Dr. Daniel R. Ashford"></div><p class="doctor__name">Daniel R. Ashford MD</p><p class="doctor__role">Orthopedic Surgeon</p></article>
    <article class="doctor"><div class="doctor__photo" role="img" aria-label="Portrait photo of Dr. Martin E. Hollis"></div><p class="doctor__name">Martin E. Hollis, MD</p><p class="doctor__role">Physical Medicine and<br>Rehabilitation Specialist</p></article>
    <article class="doctor"><div class="doctor__photo" role="img" aria-label="Portrait photo of Dr. Laura J. Penfield"></div><p class="doctor__name">Laura J. Penfield, MD, MS</p><p class="doctor__role">Physical Medicine and<br>Rehabilitation Specialist</p></article>
    <article class="doctor"><div class="doctor__photo" role="img" aria-label="Portrait photo of Dr. Owen T. Reyes"></div><p class="doctor__name">Owen T. Reyes, MD</p><p class="doctor__role">Orthopedic Surgeon</p></article>
    <article class="doctor"><div class="doctor__photo" role="img" aria-label="Portrait photo of Dr. Gregory L. Vance"></div><p class="doctor__name">Gregory L. Vance, MD</p><p class="doctor__role">Orthopedic Surgeon<br>Specializing in Spine</p></article>
    <article class="doctor"><div class="doctor__photo" role="img" aria-label="Portrait photo of Dr. Samuel K. Ortiz, Jr."></div><p class="doctor__name">Samuel K. Ortiz, Jr., MD</p><p class="doctor__role">Orthopedic Surgeon and Sports<br>Medicine and Shoulder Specialist</p></article>
    <article class="doctor"><div class="doctor__photo" role="img" aria-label="Portrait photo of Dr. Laura J. Penfield"></div><p class="doctor__name">Laura J. Penfield, MD, MS</p><p class="doctor__role">Physical Medicine and<br>Rehabilitation Specialist</p></article>
    <article class="doctor"><div class="doctor__photo doctor__photo--dark" role="img" aria-label="Portrait photo placeholder for Dr. Nathan P. Corwell"></div><p class="doctor__name">Nathan P. Corwell, MD</p><p class="doctor__role">Orthopedic Surgeon</p></article>
  </div>

  <p class="about">Northgate Bone &amp; Spine Care Center provides leading-edge, results-based care for orthopedic and spine disorders. We are a comprehensive, premier team of specialists dedicated to the diagnosis, treatment, rehabilitation and prevention of sports and orthopedic injuries and conditions. Our team is dedicated to improving the quality of life for our patients and their families.</p>
</section>

<section class="page page--back" aria-label="Back: location and contact">
  <svg class="back-header" viewBox="0 0 477 130" aria-hidden="true">
    <defs>
      <linearGradient id="backBlue" x1="0" y1="0" x2="1" y2="0.3">
        <stop offset="0" stop-color="#1d5fc2"/>
        <stop offset="0.45" stop-color="#0b3a8a"/>
        <stop offset="1" stop-color="#061633"/>
      </linearGradient>
    </defs>
    <rect width="477" height="130" fill="url(#backBlue)"/>
  </svg>
  <div class="map" role="img" aria-label="Street map showing the practice location"></div>
  <svg class="map-cover" viewBox="0 0 477 130" aria-hidden="true">
    <defs>
      <linearGradient id="backBlue2" x1="0" y1="0" x2="1" y2="0.3">
        <stop offset="0" stop-color="#1d5fc2"/>
        <stop offset="0.45" stop-color="#0b3a8a"/>
        <stop offset="1" stop-color="#061633"/>
      </linearGradient>
      <linearGradient id="silverWave" x1="0" y1="0" x2="1" y2="0">
        <stop offset="0" stop-color="#ffffff"/>
        <stop offset="0.5" stop-color="#aeb3bb"/>
        <stop offset="1" stop-color="#eef0f3"/>
      </linearGradient>
    </defs>
    <path d="M0 150 L0 0 L477 0 L477 92 C340 96 200 100 120 116 C70 126 30 138 0 150 Z" fill="url(#silverWave)"/>
    <path d="M0 142 L0 0 L477 0 L477 86 C340 90 200 94 120 110 C70 120 30 130 0 142 Z" fill="url(#backBlue2)"/>
  </svg>
  <h1 class="back-title">Our Location</h1>
  <div class="silver-strip"></div>

  <header class="brand back-brand">
    <div class="brand__name-row"><span class="brand__dot"></span><div class="brand__name">Northgate Bone &amp; Spine<br>Care Center</div></div>
    <p class="brand__sub">Northgate Bone &amp; Spine Care Center</p>
    <p class="brand__line">2450 W. Meadow Road, Ste. 210, Riverton, MO 63999</p>
    <p class="brand__phone">Phone: 555-204-7731 | www.ngspine.com</p>
  </header>

  <div class="callout">
    <p class="callout__main">Call Us TODAY <span>+1 555-204-7731</span></p>
    <p class="callout__hours">Open Weekdays from 8am to 5 pm</p>
  </div>
</section>

</body>
</html>
```